Napa Winery - Chardonnay wine label

We are looking for a label for a new Napa Valley winery - chardonnay wine. The winery is "Harrowgate Ridge Vintners" and we would like to see it depicted on a white wine (chardonnay style) bottle. The winery is called Harrowgate Ridge Vintners.

We are open to ideas!

Target Market(s)

High-end chardonnay lovers

Requirements
Nice to have
• Painted or etched label onto bottle

```html
<!DOCTYPE html>
<html lang="en">
<head>
<meta charset="utf-8">
<title>Chardonnay Label – Harrowgate Ridge Vintners</title>
<link rel="stylesheet" href="https://fonts.googleapis.com/css2?family=Electrolize&family=Oswald:wght@500&display=swap">
<style>
  :root {
    --canvas-bg: #ffffff;
    --label-black: #000000;
    --frame-red: #a3161b;
    --text-white: #f4f4f4;
    --leaf-green: #58b23c;
    --grape-peach: #f2b98a;
    --grape-orange: #e8781c;
  }
  * { margin: 0; padding: 0; box-sizing: border-box; }
  html, body {
    width: 1200px;
    height: 848px;
    overflow: hidden;
    background: var(--canvas-bg);
  }
  .canvas {
    position: relative;
    width: 1200px;
    height: 848px;
  }
  .wine-label {
    position: absolute;
    left: 301px;
    top: 250px;
    width: 598px;
    height: 335px;
    background: var(--label-black);
  }
  .label-frame {
    position: absolute;
    inset: 0;
    z-index: 2;
  }
  .varietal {
    position: absolute;
    left: 32px;
    top: 88px;
    font-family: "Electrolize", sans-serif;
    font-weight: 400;
    font-size: 54px;
    line-height: 1;
    color: var(--text-white);
    letter-spacing: 2px;
    white-space: nowrap;
  }
  .winery-name {
    position: absolute;
    left: 35px;
    top: 154px;
    font-family: "Oswald", sans-serif;
    font-weight: 500;
    font-size: 22px;
    line-height: 1.2;
    color: var(--text-white);
    letter-spacing: 0.5px;
    word-spacing: 6px;
    white-space: nowrap;
  }
  .title-rule {
    position: absolute;
    left: 34px;
    top: 196px;
    width: 296px;
    height: 3px;
    background: var(--frame-red);
  }
  .region {
    position: absolute;
    left: 50px;
    top: 244px;
    font-family: "Oswald", sans-serif;
    font-weight: 500;
    font-size: 18px;
    line-height: 1.2;
    color: var(--text-white);
  }
  .grape-cluster {
    position: absolute;
    left: 368px;
    top: 18px;
    width: 184px;
    height: 300px;
    z-index: 1;
    background: linear-gradient(180deg, var(--leaf-green) 0%, var(--leaf-green) 26%, var(--grape-peach) 40%, var(--grape-orange) 100%);
    opacity: 0.85;
  }
</style>
</head>
<body>
<main class="canvas">
  <section class="wine-label">
    <svg class="label-frame" width="598" height="335" viewBox="0 0 598 335" aria-hidden="true">
      <path d="M42 12 H556 A30 30 0 0 0 586 42 V293 A30 30 0 0 0 556 323 H42 A30 30 0 0 0 12 293 V42 A30 30 0 0 0 42 12 Z"
            fill="none" stroke="var(--frame-red)" stroke-width="3"/>
    </svg>
    <div class="grape-cluster" role="img" aria-label="Stylised grape cluster with green vine leaves above orange grapes"></div>
    <h1 class="varietal">Chardonnay</h1>
    <p class="winery-name">HARROWGATE RIDGE VINTNERS</p>
    <div class="title-rule"></div>
    <p class="region">NAPA VALLEY</p>
  </section>
</main>
</body>
</html>
```